Financial Advisor Resource Firm needs business card design

Need business card design for company in Omaha NE called Tallowbrook Partners. We provide resources to financial advisors....workshop programs, retirement analysis, and insurance planning. I would like to see designs that use grays, greens, black, and white colors. The final design should communicate 'collaboration' and be simple yet attractive to financial planning clients. I will attached our logo and another picture of a puzzle piece coming together. I would like the incorporate the puzzle picture somehow, maybe on the back somehow, with color or just the gray scale....OR, the picture be the front of the card with 'Tallowbrook' definition on it (see upload) and then company logo, employee name, title, address on the back (see ppt uploaded). The following disclosure needs to be included somewhere- Advisory services offered through Marlowe Ridge Advisors, LLC.
Updates

I uploaded a svg and ai file of the logo

Target Market(s)

Financial planning clients and financial advisors....so pretty diverse age range of about 40-70.

Industry/Entity Type

Financial Planning

Contact Information for Business Card

Dennis K. Holloway, MBA
Founder/President
5727 E. Larkspur Avenue
Suite 418
Omaha, NE 68297
Phone- (402) 555-0147
Cell- (402) 555-0183
Fax- (402) 555-0129
email- dennis@tallowbrookgroup.example
web address- www.tallowbrookgroup.example

Colors
1b1b1b
474747
d3d3d3
ffffff
9bcb3c
abd036

Requirements
Must have
• Must include logo provided, must be 2 sided, and must have disclosure...all of these items listed in project description

```html
<!DOCTYPE html>
<html lang="en">
<head>
<meta charset="utf-8">
<title>Tallowbrook Partners – Business Card</title>
<link rel="stylesheet" href="https://fonts.googleapis.com/css2?family=Cinzel:wght@400;500&family=Roboto:wght@400;500;700&display=swap">
<style>
  :root {
    --ink: #1b1b1b;
    --charcoal: #474747;
    --mist: #d3d3d3;
    --paper: #ffffff;
    --leaf: #9bcb3c;
    --lime: #abd036;
    --stage: #eceeea;
  }
  * { margin: 0; padding: 0; box-sizing: border-box; }
  html, body {
    width: 1200px; height: 835px; overflow: hidden;
    background: var(--stage);
  }
  .canvas {
    position: relative; width: 1200px; height: 835px;
    display: flex; align-items: center; justify-content: center; gap: 40px;
  }
  .card {
    position: relative; width: 540px; height: 309px; overflow: hidden;
    border-radius: 3px;
    box-shadow: 0 6px 18px rgba(0,0,0,.18);
  }

  /* Front: definition side */
  .card-front { background: var(--ink); color: var(--paper); }
  .front-texture {
    position: absolute; inset: 0;
    background: radial-gradient(ellipse at 60% 40%, #2e2e2e 0%, #1f1f1f 55%, var(--ink) 100%);
  }
  .definition {
    position: absolute; left: 0; right: 0; top: 92px; text-align: center;
  }
  .definition-word {
    font-family: "Cinzel", serif; font-weight: 400;
    font-size: 50px; letter-spacing: 1px; color: var(--lime); line-height: 1;
  }
  .definition-phonetic {
    margin-top: 14px;
    font-family: "Roboto", sans-serif; font-weight: 500; font-size: 17px; color: var(--paper);
  }
  .definition-meaning {
    margin-top: 16px;
    font-family: "Roboto", sans-serif; font-weight: 500; font-size: 13px; color: #e6e6e6;
  }

  /* Back: contact side */
  .card-back { background: var(--paper); }
  .back-shapes { position: absolute; inset: 0; }
  .contact {
    position: absolute; left: 30px; top: 26px;
    font-family: "Roboto", sans-serif; color: var(--ink);
  }
  .contact-name { font-weight: 700; font-size: 22px; line-height: 1.1; }
  .contact-title { font-weight: 400; font-size: 12.5px; letter-spacing: .5px; margin-top: 3px; }
  .contact-list { list-style: none; margin-top: 18px; }
  .contact-list li {
    display: flex; align-items: flex-start; gap: 10px;
    font-size: 13.5px; line-height: 1.25; margin-bottom: 5px;
  }
  .contact-icon { width: 14px; height: 14px; flex: none; margin-top: 1px; fill: var(--ink); }
  .disclosure {
    position: absolute; left: 30px; top: 280px; width: 300px;
    font-family: "Roboto", sans-serif; font-weight: 400; font-size: 8.5px;
    line-height: 1.2; color: var(--ink); white-space: nowrap;
  }
  .brand {
    position: absolute; left: 377px; top: 203px; width: 138px;
    display: flex; align-items: center; justify-content: center; gap: 6px;
    font-family: "Roboto", sans-serif; font-weight: 700; font-size: 15px;
    line-height: 1.1; color: var(--ink);
  }
  .brand-dot { width: 10px; height: 10px; border-radius: 50%; background: var(--leaf); flex: none; }
</style>
</head>
<body>
<main class="canvas">

  <section class="card card-front" aria-label="Card front">
    <div class="front-texture" role="img" aria-label="Faint grayscale photo of puzzle pieces coming together"></div>
    <div class="definition">
      <div class="definition-word">TALLOW·BROOK</div>
      <div class="definition-phonetic">ˈtaloʊ brʊk</div>
      <div class="definition-meaning">: to come together and unite in common interest and focus</div>
    </div>
  </section>

  <section class="card card-back" aria-label="Card back">
    <svg class="back-shapes" width="540" height="309" viewBox="0 0 540 309">
      <defs>
        <linearGradient id="panel-shade" x1="0" y1="0" x2="1" y2="1">
          <stop offset="0" stop-color="#ffffff" stop-opacity=".10"/>
          <stop offset="1" stop-color="#000000" stop-opacity=".06"/>
        </linearGradient>
      </defs>
      <polygon points="380,309 540,309 540,220" fill="var(--mist)"/>
      <polygon points="0,0 400,0 540,110 540,140 330,309 0,309" fill="var(--lime)"/>
      <g role="img" aria-label="Faint photo of puzzle pieces blended into the green panel">
        <polygon points="0,0 400,0 540,110 540,140 330,309 0,309" fill="url(#panel-shade)"/>
      </g>
      <polygon points="410,0 455,0 540,62 540,86" fill="var(--charcoal)"/>
      <circle cx="440" cy="215" r="84" fill="var(--charcoal)"/>
      <circle cx="446" cy="221" r="74" fill="var(--paper)"/>
    </svg>

    <div class="contact">
      <div class="contact-name">Dennis K. Holloway, MBA</div>
      <div class="contact-title">FOUNDER/PRESIDENT</div>
      <ul class="contact-list">
        <li><svg class="contact-icon" viewBox="0 0 24 24"><path d="M6.6 10.8a15 15 0 0 0 6.6 6.6l2.2-2.2c.3-.3.7-.4 1-.2 1.1.4 2.3.6 3.6.6.6 0 1 .4 1 1V20c0 .6-.4 1-1 1A17 17 0 0 1 3 4c0-.6.4-1 1-1h3.5c.6 0 1 .4 1 1 0 1.3.2 2.5.6 3.6.1.3 0 .7-.2 1z"/></svg>(402) 555-0147</li>
        <li><svg class="contact-icon" viewBox="0 0 24 24"><path d="M7 1h10a2 2 0 0 1 2 2v18a2 2 0 0 1-2 2H7a2 2 0 0 1-2-2V3a2 2 0 0 1 2-2zm0 3v15h10V4zm5 16.2a1 1 0 1 0 0 .1z"/></svg>(402) 555-0183</li>
        <li><svg class="contact-icon" viewBox="0 0 24 24"><path d="M6 2h12v5H6zM4 8h16a2 2 0 0 1 2 2v7h-4v5H6v-5H2v-7a2 2 0 0 1 2-2zm4 8v4h8v-4z"/></svg>(402) 555-0129</li>
        <li><svg class="contact-icon" viewBox="0 0 24 24"><path d="M2 5h20v14H2zm2 2v.5l8 5 8-5V7l-8 5z"/></svg>dennis@tallowbrookgroup.example</li>
        <li><svg class="contact-icon" viewBox="0 0 24 24"><path d="M12 2a10 10 0 1 0 0 20 10 10 0 0 0 0-20zm6.9 9h-3a15 15 0 0 0-1.3-6 8 8 0 0 1 4.3 6zM12 4c.9 1.3 1.7 3.8 1.9 7h-3.8c.2-3.2 1-5.7 1.900-7zM9.4 5a15 15 0 0 0-1.3 6h-3a8 8 0 0 1 4.3-6zM5.1 13h3a15 15 0 0 0 1.3 6 8 8 0 0 1-4.3-6zM12 20c-.9-1.3-1.7-3.8-1.9-7h3.8c-.2 3.2-1 5.7-1.9 7zm2.6-1a15 15 0 0 0 1.3-6h3a8 8 0 0 1-4.3 6z"/></svg>www.tallowbrookgroup.example</li>
        <li><svg class="contact-icon" viewBox="0 0 24 24"><path d="M12 2a7 7 0 0 0-7 7c0 5 7 13 7 13s7-8 7-13a7 7 0 0 0-7-7zm0 9.5a2.5 2.5 0 1 1 0-5 2.5 2.5 0 0 1 0 5z"/></svg><span>5727 E. Larkspur Avenue Suite 418<br>Omaha, NE 68297</span></li>
      </ul>
    </div>

    <p class="disclosure">Advisory services offered through Marlowe Ridge Advisors, LLC.</p>

    <div class="brand"><span class="brand-dot"></span><span>Tallowbrook Partners</span></div>
  </section>

</main>
</body>
</html>
```